4 x 9 Rack Card Design: Cheer Each Game Advertising Campaign

We would like a 4 x 9 Rack Card Designed using our logo as the basis for the design. We would like to incorporate the images of the shoes & the colors that are on our logo. We are attaching an image of the logo for your use.

The design should use both the front & back of the 4 x 9 card.

All text & fonts should be in "comic sans".

The card should have a fun, youthful, cartoon feel to it.

We would like the following information on the card:

Our Tag Line: Charity providing Athletic Footwear to Kids

Our Catch Phrase: "Cheer Each Game". Please include small images of various sports balls under, or around or near the catch phrase. Please use images of a Basketball, baseball, golf ball, soccer ball, Hockey Puck, American Football, Tennis ball.

Our Contact Information: PO Box 57392, Phoenix, AZ 85077; phone 480.312.4456; www.hop-and-laces.org; also use the "find us on chatterbook" image.

Who we are: We are a 501(c)3 non-profit organization providing athletic footwear to disadvantaged and at-risk youth. The proper footwear allows participation in sports activities providing a healthy outlet for energy, increased self confidence, reduced juvenile crime rates, decline in alcohol, tobacco and drug dependency, strengthened relationships and enhanced academic performance.

A Recipe: We are working on a recipe to be included. In the meantime, we are asking for designs that include a small area for a recipe on the back of the card. The recipe will be easy, with very few ingredients & instructions, so it won't take up too much space on the rack card.

Target Market(s)

Sponsors, endorsers, donators, sports teams.

Industry/Entity Type

Non-Profit

Font styles to use
Other font styles liked:
• Comic Sans

Requirements
Must have
• See project descripion
Nice to have
• See project description. Also, please take a look at our website at www.hop-and-laces.com for our style & additional information about our organization.

```html
<!DOCTYPE html>
<html lang="en">
<head>
<meta charset="utf-8">
<title>Hop-N-Laces Rack Card</title>
<link href="https://fonts.googleapis.com/css2?family=Comic+Neue:wght@400;700&family=Lato:wght@400;700&display=swap" rel="stylesheet">
<style>
  :root {
    --bg: #c9d1da;
    --paper: #f7f7f5;
    --green: #8cc63f;
    --green-dark: #6fa82b;
    --blue: #1f87c6;
    --orange: #e8781e;
    --ochre: #c98f1c;
    --red: #e0325a;
    --text: #5a5a5a;
    --burst: #1b7fc0;
    --burst-dark: #14649a;
  }
  * { box-sizing: border-box; margin: 0; padding: 0; }
  html, body { width: 1200px; height: 1108px; overflow: hidden; }
  body {
    background: var(--bg);
    font-family: "Comic Neue", "Comic Sans MS", cursive;
    color: var(--text);
    position: relative;
  }
  .card {
    position: absolute;
    top: 60px;
    width: 438px;
    height: 986px;
    background: var(--paper);
    overflow: hidden;
  }
  .card--front { left: 74px; }
  .card--back { left: 688px; }
  .card__stripe { position: absolute; left: 0; top: 0; width: 100%; height: 10px; background: var(--green); }
  .abs { position: absolute; }
  .shoes-art {
    background: linear-gradient(90deg, #2c8fd0 0%, #f08a24 25%, #f4c21a 50%, #7cc04a 72%, #f06f92 100%);
    opacity: .85;
    border-radius: 10px;
  }
  .brand-name {
    position: absolute; left: 0; width: 100%; text-align: center;
    font-weight: 700; color: var(--blue); letter-spacing: 2px;
  }
  .tagline {
    position: absolute; left: 0; width: 100%; text-align: center;
    color: var(--orange);
  }
  .purpose-btn {
    left: 127px; top: 229px; width: 173px; height: 30px;
    background: var(--green); color: #fff;
    font-family: "Lato", sans-serif; font-size: 16px;
    display: flex; align-items: center; justify-content: center;
    box-shadow: 0 3px 4px rgba(0,0,0,.25);
  }
  .purpose-text, .closing-text {
    left: 24px; width: 400px; color: var(--ochre);
    font-weight: 700; font-size: 13px; line-height: 18.5px;
  }
  .purpose-text { top: 280px; }
  .closing-text { top: 878px; }
  .list-block { left: 24px; font-size: 13px; line-height: 18.4px; }
  .list-block h3 { font-size: 13.5px; font-weight: 400; }
  .list-block ul { list-style: none; }
  .rewards { top: 340px; }
  .rewards h3 { color: var(--blue); }
  .outcomes { top: 543px; }
  .outcomes h3 { color: var(--red); }
  .benefits { top: 727px; }
  .benefits h3 { color: var(--green-dark); }
  .ball { position: absolute; border-radius: 50%; }
  .ball--football { left: 301px; top: 354px; width: 76px; height: 60px; background: #f2c21b; border-radius: 50% / 50%; transform: rotate(-30deg); }
  .ball--volley { left: 341px; top: 476px; width: 64px; height: 62px; background: linear-gradient(#e64f6a 0 40%, #f2c21b 40% 70%, #2c8fd0 70%); }
  .ball--base { left: 144px; top: 738px; width: 72px; height: 72px; background: #fff; border: 3px solid var(--orange); }
  .ball--basket { left: 232px; top: 824px; width: 48px; height: 48px; background: #3597d8; }
  .ball--soccer { left: 322px; top: 786px; width: 78px; height: 76px; background: radial-gradient(circle, #f2c21b 0 25%, #fff 26% 60%, #7cc04a 61%); border: 3px solid #777; }
  .burst { left: 264px; top: 572px; width: 200px; height: 160px; }
  .burst__label {
    position: absolute; left: 0; top: 52px; width: 170px; text-align: center;
    color: #fff; font-size: 25px; line-height: 28px;
  }
  .footer {
    position: absolute; left: 0; bottom: 0; width: 100%; height: 50px;
    background: var(--green);
    display: flex; align-items: center;
  }
  .footer--front { gap: 34px; padding-left: 42px; font-size: 12.5px; }
  .footer--front .contact { display: flex; align-items: center; gap: 6px; }
  .contact--phone { color: var(--orange); }
  .contact--address { color: var(--blue); }
  .footer--back { justify-content: center; height: 46px; color: #fff; font-family: "Lato", sans-serif; font-size: 19px; letter-spacing: .5px; }
  .photo { position: absolute; }
  .photo--kick { left: 41px; top: 176px; width: 139px; height: 138px; background: linear-gradient(#4d7a3a, #6c9a3e); }
  .photo--golf { left: 41px; top: 324px; width: 139px; height: 138px; background: linear-gradient(#8fb25a, #4e8a34); }
  .photo--ball { left: 41px; top: 470px; width: 139px; height: 136px; background: linear-gradient(#c86c8a, #f2a24a 55%, #3f6f2a); }
  .photo--trail { left: 188px; top: 176px; width: 215px; height: 430px; background: linear-gradient(160deg, #e9eef2, #b4a58a 55%, #6c6a4a); }
  .section-title { left: 29px; font-size: 24px; font-weight: 700; }
  .title--who { top: 620px; color: var(--blue); }
  .title--recipe { top: 769px; color: var(--green-dark); }
  .body-copy { left: 29px; width: 382px; font-size: 12.5px; line-height: 18.4px; text-align: justify; }
  .copy--who { top: 655px; }
  .copy--recipe { top: 802px; }
  .find-us { left: 0; top: 892px; width: 100%; display: flex; justify-content: center; align-items: center; gap: 14px; color: var(--orange); font-size: 22px; font-weight: 700; }
  .find-us__dot { width: 34px; height: 34px; border-radius: 50%; background: #4a3f8f; }
</style>
</head>
<body>

<section class="card card--front">
  <div class="card__stripe"></div>
  <div class="abs shoes-art" style="left:31px; top:18px; width:375px; height:108px;" role="img" aria-label="Cartoon row of colourful sports shoes: cleat, skate, sneaker, spike and ballet slipper"></div>
  <div class="brand-name" style="top:134px; font-size:42px;">Hop-N-Laces</div>
  <div class="tagline" style="top:190px; font-size:18px;">Charity providing Athletic Footwear to Kids</div>
  <div class="abs purpose-btn">Our Purpose</div>
  <p class="abs purpose-text">To provide athletic footwear to underprivileged and at-risk children and youth, enabling them to participate in sports and other activities.</p>

  <div class="abs list-block rewards">
    <h3>The rewards:</h3>
    <ul>
      <li>Provide a positive outlet for energy</li>
      <li>Create a sense of accomplishment</li>
      <li>Teach leadership &amp; multitasking skills</li>
      <li>Improve memory and problem-solving skills</li>
      <li>Teach teamwork, cooperation &amp; respect</li>
      <li>Foster Self-Discipline</li>
      <li>Encourage goal setting &amp; healthy habits</li>
      <li>Improved family communication and values</li>
      <li>Strengthen peer social interaction and connections</li>
    </ul>
  </div>

  <div class="abs list-block outcomes">
    <h3>Proven measurable outcomes:</h3>
    <ul>
      <li>Enhanced academic performance</li>
      <li>Reduced juvenile crime rates</li>
      <li>Improved self esteem</li>
      <li>Decline in tobacco, alcohol &amp; drug use</li>
      <li>Decreased anger &amp; stress</li>
      <li>Decrease in obesity</li>
      <li>Lower teen pregnancy rates</li>
      <li>Higher high school graduation rates</li>
    </ul>
  </div>

  <div class="abs list-block benefits">
    <h3>Who benefits?</h3>
    <ul>
      <li>Everyone!</li>
      <li>Children</li>
      <li>Families</li>
      <li>Communities</li>
      <li>Employers</li>
      <li>Schools</li>
    </ul>
  </div>

  <div class="ball ball--football" role="img" aria-label="Cartoon American football"></div>
  <div class="ball ball--volley" role="img" aria-label="Cartoon volleyball"></div>
  <div class="ball ball--base" role="img" aria-label="Cartoon baseball"></div>
  <div class="ball ball--basket" role="img" aria-label="Cartoon basketball"></div>
  <div class="ball ball--soccer" role="img" aria-label="Cartoon soccer ball"></div>

  <div class="abs burst">
    <svg width="200" height="160" viewBox="0 0 200 160">
      <rect x="110" y="58" width="90" height="44" fill="var(--burst-dark)"/>
      <polygon fill="var(--burst)" points="156,79 142.8,91.5 150.2,108.1 133.2,114.6 133.7,132.7 115.6,132.2 109.1,149.2 92.5,141.8 80,155 67.5,141.8 50.9,149.2 44.4,132.2 26.3,132.7 26.8,114.6 9.8,108.1 17.2,91.5 4,79 17.2,66.5 9.8,49.9 26.8,43.4 26.3,25.3 44.4,25.8 50.9,8.8 67.5,16.2 80,3 92.5,16.2 109.1,8.8 115.6,25.8 133.7,25.3 133.2,43.4 150.2,49.9 142.8,66.5"/>
    </svg>
    <div class="burst__label">Cheer Each<br>Game</div>
  </div>

  <p class="abs closing-text">The proper athletic footware will create a difference in a child's future: Physically, emotionally &amp; economically.</p>

  <footer class="footer footer--front">
    <span class="contact contact--phone">
      <svg width="12" height="12" viewBox="0 0 24 24"><path fill="#333" d="M6.6 10.8a15 15 0 0 0 6.6 6.6l2.2-2.2c.3-.3.7-.4 1-.2 1.1.4 2.3.6 3.6.6.6 0 1 .4 1 1V20c0 .6-.4 1-1 1A17 17 0 0 1 3 4c0-.6.4-1 1-1h3.5c.6 0 1 .4 1 1 0 1.3.2 2.5.6 3.6.1.3 0 .7-.2 1z"/></svg>
      480.312.4456
    </span>
    <span class="contact contact--address">
      <svg width="10" height="13" viewBox="0 0 20 26"><path fill="#333" d="M10 0a10 10 0 0 0-10 10c0 7 10 16 10 16s10-9 10-16A10 10 0 0 0 10 0zm0 14a4 4 0 1 1 0-8 4 4 0 0 1 0 8z"/></svg>
      PO Box 57392, Phoenix, AZ 85077
    </span>
  </footer>
</section>

<section class="card card--back">
  <div class="card__stripe"></div>
  <div class="abs shoes-art" style="left:90px; top:24px; width:266px; height:66px;" role="img" aria-label="Cartoon row of colourful sports shoes"></div>
  <div class="brand-name" style="top:96px; font-size:32px;">Hop-N-Laces</div>
  <div class="tagline" style="top:138px; font-size:15px;">Charity providing Athletic Footwear to Kids</div>

  <div class="photo photo--kick" role="img" aria-label="Photo of a young player kicking a soccer ball on grass"></div>
  <div class="photo photo--golf" role="img" aria-label="Photo of young golfers on a green"></div>
  <div class="photo photo--ball" role="img" aria-label="Photo of a foot resting on a soccer ball at sunset"></div>
  <div class="photo photo--trail" role="img" aria-label="Photo of a trail running shoe stepping on a rock"></div>

  <h2 class="abs section-title title--who">Who we are:</h2>
  <p class="abs body-copy copy--who">We are a 501(c)3 non-profit organization providing athletic footwear to disadvantaged and at-risk youth. The proper footwear allows participation in sports activities providing a healthy outlet for energy, increased self confidence, reduced juvenile crime rates, decline in alcohol, tobacco and drug dependency, strengthened relationships and enhanced academic performance.</p>

  <h2 class="abs section-title title--recipe">A Recipe:</h2>
  <p class="abs body-copy copy--recipe">We are working on a recipe to be included. In the meantime, we are asking for designs that include a small area for a recipe on the back of the card. The recipe will be easy, with very few ingredients &amp; instructions, so it won't take up too much space on the rack card.</p>

  <div class="abs find-us"><span>Find us on chatterbook</span><span class="find-us__dot"></span></div>

  <footer class="footer footer--back">www.hop-and-laces.org</footer>
</section>

</body>
</html>
```